riverstonelightcare - healing business promotion

I have and energy / intuitive healing and kinesiology business. working with people who are looking for healing outside of the modern medical model, who have tried but failed in their search for understanding their conditions and why health and or happiness eludes them. the healing is done with love, patience and understanding. I am looking to be taken seriously with my presentation and to reach a person who may be deterred by the thought of angels and intuition! but to not exclude those that are attracted to that also.

Industry/Entity Type

Medical

Contact Information for Business Card

riverstonelightcare
calm clear gentle energy renewal method
tamsin corrine hale
energy healing / kinesiology and neurotraining
0417362815 07 4186 2751
home visits available for cairns and tablelands
t.chale@maildrop-example.net

Requirements
Should not have
• Primary colours

```html
<!DOCTYPE html>
<html lang="en">
<head>
<meta charset="utf-8">
<title>Riverstone Light Care – Business Card</title>
<link rel="stylesheet" href="https://fonts.googleapis.com/css2?family=Tinos:wght@400;700&family=Arimo:wght@700&display=swap">
<style>
  :root {
    --page: #ffffff;
    --card-deep: #1573bd;
    --card-mid: #4aa6de;
    --card-light: #cdeefc;
    --ink: #1d3a72;
    --ink-soft: #233f74;
    --flower-glow: rgba(255, 255, 255, 0.38);
    --shadow: rgba(0, 0, 0, 0.28);
  }
  * { margin: 0; padding: 0; box-sizing: border-box; }
  html, body {
    width: 1200px; height: 392px; overflow: hidden;
    background: var(--page);
  }
  .canvas { position: relative; width: 1200px; height: 392px; }

  .card {
    position: absolute;
    width: 543px; height: 314px;
    background: linear-gradient(90deg, var(--card-deep) 0%, var(--card-mid) 45%, var(--card-light) 100%);
    box-shadow: 3px 3px 4px var(--shadow);
    overflow: hidden;
  }
  .card--front { left: 24px; top: 42px; }
  .card--back { left: 622px; top: 38px; }

  .flower-trail {
    position: absolute; left: 0; top: 0;
    width: 150px; height: 100%;
    background: linear-gradient(90deg, var(--flower-glow), rgba(255,255,255,0.12) 70%, rgba(255,255,255,0));
  }

  .business-name {
    position: absolute; left: 162px; top: 30px;
    font-family: "Tinos", "Times New Roman", serif;
    font-weight: 700; font-size: 28px;
    color: var(--ink);
    white-space: nowrap;
  }

  .contact-list { position: absolute; left: 196px; top: 124px; list-style: none; }
  .contact-item {
    display: flex; align-items: center; gap: 8px;
    height: 37px;
    font-family: "Arimo", Arial, sans-serif;
    font-weight: 700; font-size: 20px;
    color: var(--ink-soft);
    white-space: nowrap;
  }
  .contact-icon { width: 19px; height: 16px; flex: none; }

  .service-note {
    position: absolute; right: 14px; bottom: 12px;
    font-family: "Tinos", "Times New Roman", serif;
    font-size: 19px; color: var(--ink);
    white-space: nowrap;
  }

  .back-text {
    position: absolute; left: 123px; width: 407px;
    text-align: center;
    font-family: "Tinos", "Times New Roman", serif;
    font-size: 22px; line-height: 29px;
    color: var(--ink);
  }
  .tagline { top: 99px; }
  .tagline-rule {
    position: absolute; left: 123px; top: 131px;
    width: 407px; height: 1.5px; background: var(--ink);
  }
  .practitioner { top: 135px; }
</style>
</head>
<body>
<main class="canvas">

  <section class="card card--front">
    <div class="flower-trail" role="img" aria-label="Trail of white daisies curving down from a large daisy"></div>
    <h1 class="business-name">Riverstone Light Care</h1>
    <ul class="contact-list">
      <li class="contact-item">
        <svg class="contact-icon" viewBox="0 0 19 16" aria-hidden="true"><path d="M1 5.5h9V1.5l7.5 6.5-7.5 6.5v-4H1z" fill="none" stroke="currentColor" stroke-width="1.6" stroke-linejoin="round"/></svg>
        <span>04 1736 2815</span>
      </li>
      <li class="contact-item">
        <svg class="contact-icon" viewBox="0 0 19 16" aria-hidden="true"><path d="M1 5.5h9V1.5l7.5 6.5-7.5 6.5v-4H1z" fill="none" stroke="currentColor" stroke-width="1.6" stroke-linejoin="round"/></svg>
        <span>07 4186 2751</span>
      </li>
      <li class="contact-item">
        <svg class="contact-icon" viewBox="0 0 19 16" aria-hidden="true"><path d="M1 5.5h9V1.5l7.5 6.5-7.5 6.5v-4H1z" fill="none" stroke="currentColor" stroke-width="1.6" stroke-linejoin="round"/></svg>
        <span>t.chale@maildrop-example.net</span>
      </li>
    </ul>
    <p class="service-note">home visits available for cairns and tablelands</p>
  </section>

  <section class="card card--back">
    <div class="flower-trail" role="img" aria-label="Trail of white daisies curving down from a large daisy"></div>
    <p class="back-text tagline">calm clear gentle energy renewal method</p>
    <div class="tagline-rule"></div>
    <p class="back-text practitioner">tamsin corrine hale energy healing<br>/ kinesiology and neurotraining</p>
  </section>

</main>
</body>
</html>
```